In Search of a FANTASTIC BUSINESS CARD REFRESH AND REDESIGN

I would like to redesign the current business card for my company.  There is a parent company, Brookfane Care Group, with 2 operating companies - Brookfane Homecare and Brookfane Senior Living.
I will include the current business card design, along with the 3 logos I would like incorporated.  The business card can be two sided.  I'm looking for something clean, professional, and a fresh new look.

Target Market(s)
Hospitals, social workers, insurance agents, family members of seniors
Industry/Entity Type
Healthcare
Contact Information for Business Card
Name, title of person, address, phone number, web address, email address
Look and feel
Each slider illustrates characteristics of the customer's brand and the style your logo design should communicate.

```html
<!DOCTYPE html>
<html lang="en">
<head>
<meta charset="utf-8">
<title>Brookfane Care Group – Business Card</title>
<link href="https://fonts.googleapis.com/css2?family=Poppins:wght@400;500;600;700&display=swap" rel="stylesheet">
<style>
  :root {
    --backdrop: #808080;
    --teal: #5a9693;
    --teal-light: #dbe9e8;
    --blush: #ffdfe0;
    --pink: #f79ea0;
    --ink: #2b2b2b;
    --black: #111111;
    --white: #ffffff;
    --outline: rgba(150, 150, 150, 0.35);
  }
  * { box-sizing: border-box; margin: 0; padding: 0; }
  html, body { width: 1200px; height: 1000px; overflow: hidden; }
  body {
    background: var(--backdrop);
    font-family: "Poppins", sans-serif;
    position: relative;
  }
  .card {
    position: absolute;
    left: 294px;
    width: 613px;
    height: 352px;
    border-radius: 18px;
    overflow: hidden;
    box-shadow: 0 10px 24px rgba(0,0,0,0.35);
  }
  .card-front {
    top: 80px;
    background: var(--teal);
    display: flex;
    align-items: center;
    justify-content: center;
  }
  .front-brand {
    display: flex;
    flex-direction: column;
    align-items: center;
    gap: 14px;
  }
  .front-brand__square {
    width: 64px;
    height: 64px;
    border-radius: 12px;
    background: var(--white);
  }
  .front-brand__name {
    color: var(--white);
    font-weight: 600;
    font-size: 20px;
    letter-spacing: 0.5px;
  }

  .card-back {
    top: 524px;
    background: linear-gradient(125deg, var(--teal-light) 0%, var(--white) 32%, var(--white) 55%, var(--blush) 100%);
  }
  .back-frame {
    position: absolute;
    left: 340px;
    top: 30px;
    width: 300px;
    height: 240px;
    border: 2px solid var(--outline);
    border-radius: 30px;
    transform: rotate(-8deg);
  }
  .back-content {
    position: absolute;
    left: 30px;
    top: 32px;
    width: 270px;
    text-align: center;
  }
  .brand-row {
    display: flex;
    justify-content: space-between;
    align-items: flex-start;
    margin-bottom: 20px;
  }
  .brand-mark {
    width: 84px;
    display: flex;
    flex-direction: column;
    align-items: center;
    gap: 5px;
  }
  .brand-mark__square {
    width: 22px;
    height: 22px;
    border-radius: 4px;
  }
  .brand-mark__name {
    font-size: 10.5px;
    line-height: 1.2;
    font-weight: 500;
  }
  .brand-mark--homecare .brand-mark__square { background: var(--pink); }
  .brand-mark--homecare .brand-mark__name { color: #666; }
  .brand-mark--group .brand-mark__square { background: var(--black); }
  .brand-mark--group .brand-mark__name { color: var(--black); }
  .brand-mark--living .brand-mark__square { background: var(--teal); }
  .brand-mark--living .brand-mark__name { color: var(--teal); }

  .person-name {
    color: var(--teal);
    font-weight: 600;
    font-size: 23px;
    line-height: 1.2;
  }
  .person-title {
    color: var(--ink);
    font-size: 13.5px;
    margin-bottom: 8px;
  }
  .contact-icons {
    display: flex;
    justify-content: center;
    gap: 4px;
    margin-bottom: 6px;
  }
  .contact-icons svg { width: 24px; height: 24px; display: block; }
  .contact-lines, .address {
    color: var(--ink);
    font-size: 12px;
    line-height: 15px;
  }
  .address { margin-top: 13px; }
  .website {
    margin-top: 12px;
    font-size: 14px;
    color: var(--ink);
  }
  .website strong { color: var(--teal); font-weight: 700; }
</style>
</head>
<body>

<section class="card card-front">
  <div class="front-brand">
    <div class="front-brand__square"></div>
    <div class="front-brand__name">Brookfane Care Group</div>
  </div>
</section>

<section class="card card-back">
  <div class="back-frame"></div>
  <div class="back-content">
    <div class="brand-row">
      <div class="brand-mark brand-mark--homecare">
        <div class="brand-mark__square"></div>
        <div class="brand-mark__name">Brookfane<br>Homecare</div>
      </div>
      <div class="brand-mark brand-mark--group">
        <div class="brand-mark__square"></div>
        <div class="brand-mark__name">Brookfane<br>Care Group</div>
      </div>
      <div class="brand-mark brand-mark--living">
        <div class="brand-mark__square"></div>
        <div class="brand-mark__name">Brookfane<br>Senior Living</div>
      </div>
    </div>

    <div class="person-name">Dana Okafor</div>
    <div class="person-title">President, CEO</div>

    <div class="contact-icons">
      <svg viewBox="0 0 24 24" aria-label="Phone">
        <circle cx="12" cy="12" r="12" fill="#5a9693"/>
        <path d="M8.5 6.5c.5-.4 1.2-.3 1.5.2l1 1.7c.3.5.2 1.1-.3 1.4l-.7.5c.6 1.3 1.5 2.3 2.8 2.9l.5-.7c.3-.5 1-.6 1.4-.3l1.7 1c.5.3.6 1 .2 1.5l-.8.9c-.6.6-1.5.8-2.3.5-2.9-1.2-5-3.3-6.1-6.1-.3-.8-.1-1.7.5-2.3z" fill="#fff"/>
      </svg>
      <svg viewBox="0 0 24 24" aria-label="Fax">
        <circle cx="12" cy="12" r="12" fill="#5a9693"/>
        <rect x="8.5" y="6" width="7" height="3.5" fill="#fff"/>
        <rect x="6.5" y="10" width="11" height="5" rx="1" fill="#fff"/>
        <rect x="8.5" y="13.5" width="7" height="4.5" fill="#fff" stroke="#5a9693" stroke-width="0.8"/>
      </svg>
      <svg viewBox="0 0 24 24" aria-label="Email">
        <circle cx="12" cy="12" r="12" fill="#5a9693"/>
        <rect x="6.5" y="8" width="11" height="8" rx="0.8" fill="#fff"/>
        <path d="M6.8 8.4l5.2 4.2 5.2-4.2" fill="none" stroke="#5a9693" stroke-width="0.9"/>
      </svg>
    </div>

    <div class="contact-lines">
      (555) 014-2286<br>
      (555) 014-2290<br>
      dana@brookfanecare.com
    </div>
    <div class="address">
      480 Harbor View Ave. #210<br>
      Lakemont, HI 96800
    </div>
    <div class="website"><strong>brookfanecare</strong>.com</div>
  </div>
</section>

</body>
</html>
```